Labels/logo for luxury bath products

I am developing a range of luxury bath foams - aimed at the top end of the luxury market. My company name is VEM (very basic website can be seen at www.vemarton.example).

I am looking for a label design for the front of the bottle, which should incorporate the VEM logo as per the website (file attached), but embedded within a more intricate label design. I provide a link to a picture of the bottle below.

The bath foam will come in four fragrances: Vetiver, Sandalwood, Jasmine and Neroli. The label should include the fragrance name. So the label must include the brand name 'VEM' and the name of the fragrance - e.g. Sandalwood Bath Foam, Neroli Bath Foam, etc.

The products are aimed at both the male and female market and so shouldn't be too feminine.

A brand to take inspiration from is Lune Bravière: http://www.lunebraviere.example/ - I like the labels that they use on their products, which is a gold embossed crest, which they use as the label for their products. I am not referring to their font, but to their label design - I like the embossed label, and am quite keen on metallics.

Conversely, I would like to add a contemporary edge to this design - I like the striping and contemporary fonts on this design: http://www.hadley-frost.example/images/fac83.jpg

My brand also harnesses the powers of natural flower ingredients, and so I am inspired by the products of Quenby - quenby.example. This labelling is more clinical and scientific.

Ideally I would like a label which combines these elements - i.e. a luxury label with a contemporary feel, that incorporate the scientific nature of the product.

The design needs to communicate high end luxury. The bottle is however apothecary style, and a nod to science and botany would be good. I would however like a bold approach to this design - it is a modern brand.

The bottle being used for the product can be seen at: http://www.tavel-vitro.example/en/product-groups/8-Apothecary-bottles - these are extremely expensive bottles and the label needs to reflect this quality. These bottles are traditional in design, but incorporate high end glassware technology to preserve the integrity of the natural ingredients. Therefore the product is a mix of old and new, and the label could also reflect this. The colour of the glass is very deep purple.

The front label does not need information such as weight/volume - it purely needs a label which will recognise it as the VEM brand, with the product name. I am looking for a high quality label, which is unique. I am happy to print embossed labels and to use foils on my labels.

Please do not be boring! I appreciate I have given a variety of influences, so summarise the requirements are a mix of:

a bold design
contemporary
luxury

The label must include NO slogans.

I am looking to build a relationship with a graphic designer for packaging and website design requirements so this will be the first of many projects.

Target Market(s)

Luxury end of market - clientele will like luxury and will pay for the highest quality ingredients in the product, but will also appreciate the botanical nature of the product.

Industry/Entity Type

Graphic Designer

Requirements
Must have
• Must include the company name, VEM, although this doesn't need to be particularly prominent. And the product name, e.g. Sandalwood.
Nice to have
• It should combine luxury, but with recognition of the science behind the product.
Should not have
• No slogans, minimal wording on the front label. No other wording other than company name and product name. No primary colours.

```html
<!DOCTYPE html>
<html lang="en">
<head>
<meta charset="utf-8">
<title>VEM Vetiver Bath Foam – Front Label</title>
<link href="https://fonts.googleapis.com/css2?family=Montserrat:wght@700&family=Parisienne&display=swap" rel="stylesheet">
<style>
  :root {
    --backdrop: #f1f1f3;
    --frame-cream: #f7e9a9;
    --frame-edge: #e6cf7d;
    --gold-light: #e2bb83;
    --gold-mid: #c99a5c;
    --gold-deep: #b07f45;
    --ink-cream: #fbf0c0;
    --ornament-glow: #fbf0c8;
  }
  html, body {
    margin: 0;
    padding: 0;
    width: 1200px;
    height: 898px;
    overflow: hidden;
    background: var(--backdrop);
  }
  .canvas {
    position: relative;
    width: 1200px;
    height: 898px;
    display: flex;
    align-items: center;
    justify-content: center;
  }
  .label {
    width: 506px;
    height: 600px;
    display: block;
  }
  .frame-outer { fill: var(--frame-cream); stroke: var(--frame-edge); stroke-width: 1; }
  .frame-inner-line { fill: none; stroke: var(--ink-cream); stroke-width: 1.2; }
  .label-field { fill: url(#goldField); }
  .ornament-crown { fill: url(#ornamentGlow); }
  .ornament-band { fill: url(#ornamentBand); }
  .brand-name {
    font-family: "Montserrat", Arial, sans-serif;
    font-weight: 700;
    font-size: 40px;
    fill: var(--ink-cream);
    letter-spacing: -0.5px;
  }
  .product-name {
    font-family: "Parisienne", cursive;
    font-size: 19px;
    fill: var(--ink-cream);
  }
</style>
</head>
<body>
<main class="canvas">
  <svg class="label" viewBox="0 0 270 320" xmlns="http://www.w3.org/2000/svg" aria-labelledby="labelTitle">
    <title id="labelTitle">VEM Vetiver Bath Foam label</title>
    <defs>
      <linearGradient id="goldField" x1="0" y1="0" x2="1" y2="1">
        <stop offset="0" stop-color="var(--gold-light)"/>
        <stop offset="0.55" stop-color="var(--gold-mid)"/>
        <stop offset="1" stop-color="var(--gold-deep)"/>
      </linearGradient>
      <radialGradient id="ornamentGlow" cx="0.5" cy="0.5" r="0.5">
        <stop offset="0" stop-color="var(--ornament-glow)" stop-opacity="0.32"/>
        <stop offset="0.7" stop-color="var(--ornament-glow)" stop-opacity="0.14"/>
        <stop offset="1" stop-color="var(--ornament-glow)" stop-opacity="0"/>
      </radialGradient>
      <radialGradient id="ornamentBand" cx="0.5" cy="0.5" r="0.5">
        <stop offset="0" stop-color="var(--ornament-glow)" stop-opacity="0.3"/>
        <stop offset="1" stop-color="var(--ornament-glow)" stop-opacity="0"/>
      </radialGradient>
      <path id="crestShape" d="M135,0 C165,0 185,12 190,30 C215,28 240,45 245,80 L245,95 L258,95 L258,140 C270,150 270,175 270,200 C270,270 210,320 135,320 C60,320 0,270 0,200 C0,175 0,150 12,140 L12,95 L25,95 L25,80 C30,45 55,28 80,30 C85,12 105,0 135,0 Z"/>
    </defs>

    <use href="#crestShape" class="frame-outer"/>
    <use href="#crestShape" class="label-field" transform="translate(10.8 12.8) scale(0.92)"/>
    <use href="#crestShape" class="frame-inner-line" transform="translate(18.9 22.4) scale(0.86)"/>

    <ellipse class="ornament-crown" role="img" aria-label="Ornamental baroque scrollwork framing the top of the crest"
             cx="135" cy="112" rx="100" ry="70"/>
    <ellipse class="ornament-band" role="img" aria-label="Ornamental scrollwork band beneath the brand name"
             cx="135" cy="186" rx="95" ry="14"/>

    <text class="brand-name" x="135" y="162" text-anchor="middle">VEM</text>
    <text class="product-name" x="135" y="243" text-anchor="middle">Vetiver</text>
    <text class="product-name" x="135" y="264" text-anchor="middle">Bath Foam</text>
  </svg>
</main>
</body>
</html>
```